依頼概要
■依頼の目的/概要
弊社が販売予定している玄米コーヒー(ドリップ式)のラベルデザインをお願いします。弊社は、森川緑風農園といいまして、自然農法栽培でお米や野菜を作っている農家です。信条は「土がきれいになれば世界が平和になる」です。今回の商品は健康食品としての位置づけになります。

■依頼詳細
今回は弊社が販売する玄米コーヒー(ドリップ式)のラベルのデザインをお願いします。
すでに、インスタント式の玄米コーヒーを販売しており、今回の商品はそれに続くプレミアム玄米コーヒーとして、前回よりも一段格上の商品を考えております。インスタント式は粉状ですが、今回の商品は粗挽きで本当の粗挽きコーヒーとほとんど変わらない色と形状です。入れた玄米コーヒーの色も、何も言わなければ本当のコーヒーと見分けがつきません。味もドリップ式はとっても美味しく、一度飲むと病みつきになります。

プレミアム玄米コーヒー(ドリップ式)の特徴は以下のとおりです。

●本当のコーヒーのようにドリップ式で美味しい玄米コーヒーが入れられます。
●使用している玄米は、自然農法栽培で作った、無肥料、無農薬のこだわりのお米を100%使用しています。
●コーヒーといっても、玄米飲料なのでノンカフェインで身体に優しいです。
●ポリフェノールや食物繊維が豊富に含まれていて、健康志向の人にはぴったりの飲料です。
●玄米には解毒作用があるようで、お通じが良くなり、身体の中をスッキリきれいにしてくれます。
(ちなみに初めて飲む方のなかには、下痢をされる方が多くいらっしゃいます。わたしもその一人でした。)
●内容量は200gです。

■その他の要望
●前回のインスタント式の商品の写真を添付してあります。前回は白のパッケージ(半透明、和紙風)でしたが、今回は濃い茶色(つや消し)のパッケージ(添付写真参照)になっており、高級感の漂うデザインが希望です。ドリップでコーヒーを入れている美しい写真をデザインにいれていただけると嬉しいです。(一目でドリップ式と分かる)
もちろん写真以外のデザインでも結構です。
●デザインの中に、森川緑風農園のロゴマークを入れてください。ファイルを添付してあります。
●パッケージの大きさは横140㎜×縦220㎜(190㎜)のチャック付スタンド袋です。

注意:表示法の関係で「自然農法」「無肥料」「無農薬」の言葉は使えません。
「自然栽培」「自然栽培法」「肥料不使用」「化学肥料不使用」「農薬不使用」の表記ならOKです。

その他何かご不明な点がございましたら、お気軽にご質問下さい。
デザイナーの皆様、どうぞよろしくお願いいたします!!
「ドリップ式」または「ドリップ用」という言葉をデザインの中に入れてください。
「プレミアム」という言葉も英語またはカタカナで入れてください。
■ 選んだ理由

私の希望通り、ドリップのシズル感と全体的な高級感がよく表現されていました。色の使い方が大変気に入りました。素晴らしいデザインを本当にありがとうございました。
とても満足しています。
また機会がありましたら、どうぞよろしくお願いいたします。

■ 提案者全員のお礼・コメント

この度は、たくさんの提案を頂きありがとうございました。
どれもすばらしいデザインばかりでした。
機会がありましたらまたよろしくお願いいたします。

```html
<!DOCTYPE html>
<html lang="ja">
<head>
<meta charset="utf-8">
<title>プレミアム玄米珈琲 ドリップ式</title>
<link href="https://fonts.googleapis.com/css2?family=Noto+Serif+JP:wght@500;700&family=Cormorant+Garamond:wght@400;500&family=Courier+Prime&family=Noto+Sans+JP:wght@500;700&display=swap" rel="stylesheet">
<style>
  :root {
    --bg: #ffffff;
    --pouch: #6e4c3e;
    --pouch-dark: #5d3f33;
    --label: #f7f7f2;
    --gold: #c9a25a;
    --title: #5b3b2d;
    --green: #3f6d2c;
    --band-text: #ffffff;
  }
  * { margin: 0; padding: 0; box-sizing: border-box; }
  html, body { width: 700px; height: 1200px; overflow: hidden; background: var(--bg); }
  .canvas { position: relative; width: 700px; height: 1200px; }
  .pouch { position: absolute; left: 98px; top: 90px; width: 514px; height: 1040px;
    background: var(--pouch); border-radius: 10px 10px 6px 6px; }
  .pouch__seal { position: absolute; left: 0; right: 0; top: 40px; height: 3px; background: var(--pouch-dark); }
  .pouch__notch { position: absolute; top: 70px; width: 10px; height: 6px; background: var(--bg); }
  .pouch__notch--left { left: 0; border-radius: 0 3px 3px 0; }
  .pouch__notch--right { right: 0; border-radius: 3px 0 0 3px; }
  .label { position: absolute; left: 158px; top: 191px; width: 384px; height: 550px;
    background: var(--label); text-align: center; }
  .label__wheat { position: absolute; left: 170px; top: 42px; width: 44px; height: 46px;
    border-radius: 50%; background: radial-gradient(circle, rgba(201,162,90,0.55), rgba(201,162,90,0) 70%); }
  .label__premium { position: absolute; top: 96px; width: 100%;
    font-family: "Cormorant Garamond", serif; font-size: 21px; letter-spacing: 2px; color: var(--gold); }
  .label__title { position: absolute; top: 118px; width: 100%;
    font-family: "Noto Serif JP", serif; font-weight: 700; font-size: 56px; letter-spacing: 6px; color: var(--title); }
  .label__subtitle { position: absolute; top: 194px; width: 100%;
    font-family: "Courier Prime", monospace; font-size: 14px; color: var(--title); }
  .label__drip { position: absolute; right: 50px; top: 250px; text-align: center; }
  .label__drip-text { font-family: "Noto Sans JP", sans-serif; font-weight: 700; font-size: 13px; color: var(--green); display: block; margin-bottom: 6px; }
  .label__grass { position: absolute; left: 18px; top: 356px; width: 112px; height: 92px;
    background: linear-gradient(to top, #6f9a4e, #cfe2bd 80%, rgba(247,247,242,0)); }
  .label__brand { position: absolute; left: 120px; top: 402px;
    font-family: "Cormorant Garamond", serif; font-weight: 500; font-size: 36px; line-height: 1; letter-spacing: 3px; color: var(--green); }
  .label__weight { position: absolute; right: 14px; top: 420px;
    font-family: "Noto Sans JP", sans-serif; font-size: 12px; line-height: 1; color: var(--title); }
  .label__band { position: absolute; left: 0; right: 0; bottom: 0; height: 88px; background: var(--green);
    display: flex; flex-direction: column; justify-content: center; padding: 0 14px; text-align: left; }
  .label__band p { font-family: "Noto Sans JP", sans-serif; font-weight: 500; font-size: 13px; line-height: 1.7; color: var(--band-text); white-space: nowrap; }
</style>
</head>
<body>
<div class="canvas">
  <div class="pouch">
    <div class="pouch__seal"></div>
    <div class="pouch__notch pouch__notch--left"></div>
    <div class="pouch__notch pouch__notch--right"></div>
  </div>
  <section class="label">
    <div class="label__wheat" role="img" aria-label="稲穂の飾り"></div>
    <div class="label__premium">PREMIUM</div>
    <h1 class="label__title">玄米珈琲</h1>
    <div class="label__subtitle">Brown Rice Coffee</div>
    <div class="label__drip">
      <span class="label__drip-text">ドリップ式</span>
      <svg width="70" height="70" viewBox="0 0 92 92" aria-label="ドリップのアイコン">
        <circle cx="46" cy="46" r="46" fill="var(--green)"/>
        <line x1="14" y1="20" x2="78" y2="20" stroke="#fff" stroke-width="3"/>
        <path d="M26 28 H66 L46 50 Z" fill="#fff"/>
        <path d="M46 56 q-3 5 0 7 q3 -2 0 -7" fill="#fff"/>
        <rect x="44.5" y="62" width="3" height="14" fill="#fff"/>
        <path d="M34 78 H58" stroke="#fff" stroke-width="3" stroke-linecap="round"/>
      </svg>
    </div>
    <div class="label__grass" role="img" aria-label="草のイラスト"></div>
    <div class="label__brand">MEADOW</div>
    <div class="label__weight">200g</div>
    <div class="label__band">
      <p>農薬・化学肥料不使用の自然栽培玄米100%使用。</p>
      <p>ノンカフェインで食物繊維が豊富な玄米飲料です。</p>
    </div>
  </section>
</div>
</body>
</html>
```